1 Banner für Affiliate-Marketing (Börse/Trading)
Zielgruppe
Wir vermitteln Kunden an einen Broker. Die Kunden eröffnen Handelskonten, in denen sie selbständig Finanzprodukte (CFDs, Forex, Aktien, Edelmetalle,...) gehebelt handeln. Wir bieten dem Kunden eine Dienstleistung an, indem wir Broker vorauswählen, technischen Support liefern, bei der Kontoeröffnung unterstützen und auf Wunsch auch Trader ausbilden.
Zielgruppe: männlich, finanz- und risikoaffin, Spekulant
Aufgabenstellung
Wir benötigen 1 klickstarken Banner für das Affiliate-Marketing
Bannergröße: 300*250
Formate: GIF, PNG, JPG, Vektor
Gerne auch animierte Vorschläge, aber bitte nicht ausschließlich.
Zusätzliche Info, die verarbeitet werden kann (aber nicht muss): Bright Holdings hat in 2016 bei 2 Kundenumfragen den Testsieg als bester Broker gewonnen.
Design ist frei und muss sich nicht an der Homepage orientieren - vielmehr suchen wir klickstarke Banner aus der Finanz-/Börsenwelt mit Bildern Ihrer Wahl.

```html
<!DOCTYPE html>
<html lang="de">
<head>
<meta charset="utf-8">
<title>Bright Holdings – Bannerset Testsieger 2016</title>
<link rel="stylesheet" href="https://fonts.googleapis.com/css2?family=Anton&family=Ubuntu:wght@500;700&display=swap">
<style>
  :root{
    --bg:#232323;
    --navy:#0b3d63;
    --green:#0aa14a;
    --orange:#f0731f;
    --badge:#e8531c;
    --yellow:#ffd800;
    --ink:#111111;
    --white:#ffffff;
    --label:#f2f2f2;
  }
  *{margin:0;padding:0;box-sizing:border-box}
  html,body{width:1200px;height:857px;overflow:hidden;background:var(--bg)}
  .sheet{position:absolute;left:0;top:0;width:1400px;height:1000px;transform:scale(.857143);transform-origin:0 0;font-family:"Ubuntu",sans-serif}
  .size-label{position:absolute;color:var(--label);font-weight:700;font-size:17px;letter-spacing:.5px;word-spacing:3px}
  .banner{position:absolute;overflow:hidden}
  .photo{position:absolute;inset:0;background:
      radial-gradient(ellipse at 60% 85%, rgba(10,20,60,.75) 0%, rgba(10,20,60,0) 45%),
      linear-gradient(160deg,#1e8ff0 0%,#1273e0 40%,#0b57c8 70%,#183a8a 100%)}
  .shapes{position:absolute;left:0;top:0}
  .shapes .band{fill:var(--orange)}
  .shapes .field{fill:var(--green)}
  .logo-block{position:absolute;left:0;top:0;background:var(--navy)}
  .brand{position:absolute;font-family:"Anton",sans-serif;color:var(--white);line-height:1;white-space:nowrap;text-align:center}
  .kicker{position:absolute;color:var(--white);font-weight:700;line-height:1;white-space:nowrap}
  .award{position:absolute;color:var(--white);font-weight:700;line-height:.92;white-space:nowrap}
  .year{position:absolute;background:var(--yellow);color:var(--ink);font-weight:700;display:flex;align-items:center;justify-content:center;line-height:1}
  .badge{position:absolute;overflow:visible}
  .cta{position:absolute;background:var(--orange);color:var(--white);font-weight:700;display:flex;align-items:center;justify-content:center;white-space:nowrap;border-radius:2px;letter-spacing:.3px}
</style>
</head>
<body>
<svg width="0" height="0" style="position:absolute">
  <defs>
    <symbol id="seal" viewBox="0 0 100 100">
      <circle cx="50" cy="50" r="48" fill="#e8531c" stroke="#ffffff" stroke-width="1.5"/>
      <circle cx="50" cy="50" r="42" fill="none" stroke="#ffffff" stroke-width="1"/>
      <g transform="rotate(-15 50 50)" font-family="Ubuntu, sans-serif" font-weight="500" font-size="13" fill="#ffffff" text-anchor="middle">
        <text x="50" y="39">GÜNSTIGER</text>
        <text x="50" y="54">IM GER30</text>
        <text x="50" y="69">IST KEINER!</text>
      </g>
    </symbol>
  </defs>
</svg>

<div class="sheet">

  <!-- Leaderboard 728 x 90 -->
  <div class="size-label" style="left:68px;top:104px">728 X 90</div>
  <div class="banner" style="left:66px;top:142px;width:728px;height:90px">
    <div class="photo" role="img" aria-label="Börsenkurse auf Bildschirm mit Silhouetten von Händlern"></div>
    <svg class="shapes" width="728" height="90" viewBox="0 0 728 90">
      <polygon class="band" points="163,0 548,0 590,45 548,90 163,90"/>
      <polygon class="field" points="163,0 528,0 570,45 528,90 163,90"/>
    </svg>
    <div class="logo-block" style="width:163px;height:90px"></div>
    <div class="brand" style="left:0;top:10px;width:163px;font-size:33px">BRIGHT<br>HOLDINGS</div>
    <div class="kicker" style="left:206px;top:7px;font-size:19px">Testsieger</div>
    <div class="award" style="left:170px;top:33px;font-size:22px">BESTER<br>BROKER</div>
    <div class="year" style="left:272px;top:34px;width:94px;height:38px;font-size:32px">2016</div>
    <svg class="badge" style="left:378px;top:-3px" width="96" height="96" viewBox="0 0 100 100"><use href="#seal"/></svg>
    <div class="cta" style="left:594px;top:27px;width:128px;height:30px;font-size:15px">HIER KLICKEN</div>
  </div>

  <!-- Banner 468 x 60 -->
  <div class="size-label" style="left:822px;top:104px">468 X 60</div>
  <div class="banner" style="left:819px;top:142px;width:468px;height:60px">
    <div class="photo" role="img" aria-label="Börsenkurse auf Bildschirm mit Silhouetten von Händlern"></div>
    <svg class="shapes" width="468" height="60" viewBox="0 0 468 60">
      <polygon class="band" points="90,0 345,0 372,30 345,60 90,60"/>
      <polygon class="field" points="90,0 330,0 357,30 330,60 90,60"/>
    </svg>
    <div class="logo-block" style="width:90px;height:60px"></div>
    <div class="brand" style="left:0;top:8px;width:90px;font-size:21px">BRIGHT<br>HOLDINGS</div>
    <div class="kicker" style="left:135px;top:1px;font-size:15px">Testsieger</div>
    <div class="award" style="left:98px;top:19px;font-size:16px">BESTER<br>BROKER</div>
    <div class="year" style="left:170px;top:19px;width:86px;height:33px;font-size:27px">2016</div>
    <svg class="badge" style="left:264px;top:-6px" width="74" height="74" viewBox="0 0 100 100"><use href="#seal"/></svg>
    <div class="cta" style="left:372px;top:19px;width:94px;height:20px;font-size:11px">HIER KLICKEN</div>
  </div>

  <!-- Skyscraper 120 x 600 -->
  <div class="size-label" style="left:66px;top:897px">120 X 600</div>
  <div class="banner" style="left:67px;top:284px;width:120px;height:600px">
    <div class="photo" role="img" aria-label="Börsenkurse auf Bildschirm mit Silhouetten von Händlern"></div>
    <svg class="shapes" width="120" height="600" viewBox="0 0 120 600">
      <polygon class="band" points="0,72 120,72 120,320 60,350 0,320"/>
      <polygon class="field" points="0,72 120,72 120,308 60,338 0,308"/>
    </svg>
    <div class="logo-block" style="width:120px;height:72px"></div>
    <div class="brand" style="left:0;top:8px;width:120px;font-size:27px">BRIGHT<br>HOLDINGS</div>
    <div class="kicker" style="left:8px;top:83px;font-size:19px">Testsieger</div>
    <div class="award" style="left:8px;top:109px;font-size:25px">BESTER<br>BROKER</div>
    <div class="year" style="left:3px;top:160px;width:112px;height:40px;font-size:35px">2016</div>
    <svg class="badge" style="left:5px;top:212px" width="110" height="110" viewBox="0 0 100 100"><use href="#seal"/></svg>
    <div class="cta" style="left:3px;top:568px;width:113px;height:26px;font-size:13px">HIER KLICKEN</div>
  </div>

  <!-- Wide skyscraper 160 x 600 -->
  <div class="size-label" style="left:237px;top:897px">160 X 600</div>
  <div class="banner" style="left:234px;top:284px;width:160px;height:600px">
    <div class="photo" role="img" aria-label="Börsenkurse auf Bildschirm mit Silhouetten von Händlern"></div>
    <svg class="shapes" width="160" height="600" viewBox="0 0 160 600">
      <polygon class="band" points="0,70 160,70 160,322 80,354 0,322"/>
      <polygon class="field" points="0,70 160,70 160,310 80,342 0,310"/>
    </svg>
    <div class="logo-block" style="width:160px;height:70px"></div>
    <div class="brand" style="left:0;top:4px;width:160px;font-size:31px">BRIGHT<br>HOLDINGS</div>
    <div class="kicker" style="left:18px;top:82px;font-size:23px">Testsieger</div>
    <div class="award" style="left:18px;top:112px;font-size:31px">BESTER<br>BROKER</div>
    <div class="year" style="left:16px;top:170px;width:124px;height:45px;font-size:39px">2016</div>
    <svg class="badge" style="left:27px;top:220px" width="112" height="112" viewBox="0 0 100 100"><use href="#seal"/></svg>
    <div class="cta" style="left:5px;top:562px;width:150px;height:32px;font-size:18px">HIER KLICKEN</div>
  </div>

  <!-- Square 500 x 500 -->
  <div class="size-label" style="left:442px;top:809px">500 X 500</div>
  <div class="banner" style="left:438px;top:284px;width:502px;height:500px">
    <div class="photo" role="img" aria-label="Börsenkurse auf Bildschirm mit Silhouetten von Händlern"></div>
    <svg class="shapes" width="502" height="500" viewBox="0 0 502 500">
      <polygon class="band" points="0,88 502,88 502,254 251,286 0,258"/>
      <polygon class="field" points="0,88 502,88 502,240 251,272 0,244"/>
    </svg>
    <div class="logo-block" style="width:502px;height:88px"></div>
    <div class="brand" style="left:0;top:10px;width:502px;font-size:64px">BRIGHT HOLDINGS</div>
    <div class="kicker" style="left:0;top:93px;width:454px;text-align:center;font-size:36px">Testsieger</div>
    <div class="award" style="left:40px;top:142px;font-size:49px">BESTER<br>BROKER</div>
    <div class="year" style="left:241px;top:147px;width:213px;height:79px;font-size:72px">2016</div>
    <svg class="badge" style="left:172px;top:256px" width="142" height="142" viewBox="0 0 100 100"><use href="#seal"/></svg>
    <div class="cta" style="left:147px;top:446px;width:190px;height:42px;font-size:24px">HIER KLICKEN</div>
  </div>

  <!-- Medium rectangle 300 x 250 -->
  <div class="size-label" style="left:986px;top:552px">300 X 250</div>
  <div class="banner" style="left:987px;top:284px;width:300px;height:250px">
    <div class="photo" role="img" aria-label="Börsenkurse auf Bildschirm mit Silhouetten von Händlern"></div>
    <svg class="shapes" width="300" height="250" viewBox="0 0 300 250">
      <polygon class="band" points="0,50 300,50 300,151 150,168 0,162"/>
      <polygon class="field" points="0,50 300,50 300,143 150,160 0,154"/>
    </svg>
    <div class="logo-block" style="width:300px;height:50px"></div>
    <div class="brand" style="left:0;top:4px;width:300px;font-size:38px">BRIGHT HOLDINGS</div>
    <div class="kicker" style="left:0;top:57px;width:292px;text-align:center;font-size:20px">Testsieger</div>
    <div class="award" style="left:36px;top:83px;font-size:26px">BESTER<br>BROKER</div>
    <div class="year" style="left:147px;top:84px;width:111px;height:44px;font-size:40px">2016</div>
    <svg class="badge" style="left:100px;top:136px" width="96" height="96" viewBox="0 0 100 100"><use href="#seal"/></svg>
    <div class="cta" style="left:184px;top:219px;width:112px;height:25px;font-size:14px">HIER KLICKEN</div>
  </div>

</div>
</body>
</html>
```